Perfume Oil manufacturing and distribution company needs an emotion inspiring Wordpress Design

Must be Wordpress Design
Beautiful website needed for a company that manufactures and distributes scents that fragrance products from fine fragrances to personal care and household products. Please refer to attached file (namely "brief" for detailed explanation of our company, product and design requirements)

Website must be beautiful, and not too cluttered.

Must be coded for use in WordPress after design phase

remember not to flood website with pictures of perfumes and perfume bottles, this website is meant to inspire emotion...looking at the big fragrance brands (Valdoret and Morvaleth) one will not see pictures of perfume bottles etc. The site is all about emotion and smell and the senses.
Keep this in mind when submitting designs.

The site must captivate and inspire emotion with beautiful visuals.

the website must be about how one feels when surrounded by a beautiful smell, how one feels confident wearing a good scent. how freshly baked break reminds you of your grandmas house, or how a scent can remind of a seductive encounter, or a memory of fun times with friends out on the town, or as simple as the smell of a good cup of coffee or a rose to inspire a new days happenings.

all this emotion and feeling must be tied into the fact that Aroma Nest makes these moments through great smells. Which we supply to manufacturers of these great end products. whether it is a fine fragrance, a lotion, a car fragrance or a home spray. We scent the world around us.

try not to look too much at our existing website as this is outdated and the company has changed much since then, refer to this and the attached brief

Target Market(s)

small to medium businesses who manufacture products that need to be fragranced. whether these products be prestigious fine fragrances, daily personal care products or home care products, we make the fragrances that make these products beautiful.

Industry/Entity Type

Perfume

Coding

Coded - Design and coding required

Number of Pages Required

5+ page

Font styles to use
Serif
Sans Serif

Colors

Designer to choose colors to be used in the design.

Requirements
Must have
• must have full page header that captivates audience and inspires emotion (through a video or powerful imagery)
• Smell is a powerful emotion trigger and since a computer screen can not produce smell we will need to engage emotion through beautiful imagery and or video and beautiful design on the website. (refer to attached "brief" for more details)
• Must be coded for use in WordPress ONLY after design phase
• site must work well and look great on mobile since most of our audience use mobile to access our site.
Should not have
• too many pictures of perfume packaging and actual products, looking at the big fragrance manufacturers (Valdoret, Morvaleth, KTB) one will not see pictures of perfume bottles and packaging. This is very important as the website is more to inspire emotion and give a sense of how fragrance and perfume makes one feel.
• The site must captivate and inspire emotion with beautiful visuals.

```html
<!DOCTYPE html>
<html lang="en">
<head>
<meta charset="utf-8">
<title>Aroma Nest – Master Perfumers</title>
<link rel="stylesheet" href="https://fonts.googleapis.com/css2?family=Montserrat+Alternates:wght@400;500;600;700&display=swap">
<style>
:root{
  --blue:#2f9fd9;
  --ink:#2d2d2d;
  --muted:#777b80;
  --soft:#f3f5f8;
  --footer:#414141;
  --footer-text:#c9c9c9;
  --white:#ffffff;
  --line:#dfe3e8;
}
*{box-sizing:border-box;margin:0;padding:0}
html,body{width:1200px;height:2609px;overflow:hidden}
body{font-family:"Montserrat Alternates",sans-serif;color:var(--ink);background:var(--white);position:relative}
a{color:inherit;text-decoration:none}
.abs{position:absolute}

/* hero */
.hero{position:absolute;left:0;top:0;width:1200px;height:640px;
  background:radial-gradient(ellipse at 70% 30%,#6f8f3c 0%,#3f5f22 45%,#22351a 100%)}
.brand{position:absolute;display:flex;align-items:center;gap:10px;color:var(--white)}
.brand-dot{width:52px;height:52px;border-radius:50%;background:var(--white)}
.brand-name{font-size:30px;font-weight:600;line-height:1}
.brand-sub{font-size:11px;margin-top:3px}
.hero .brand{left:80px;top:36px}
.topnav{position:absolute;top:28px;right:90px;display:flex;gap:30px;font-size:12px;color:var(--white)}
.search{position:absolute;top:28px;right:80px}
.mainnav{position:absolute;top:64px;right:80px;display:flex;align-items:center;font-size:13.5px;font-weight:500;color:var(--white)}
.mainnav a{padding:0 22px;border-left:1px solid rgba(255,255,255,.5);line-height:14px}
.mainnav a:first-child{border-left:none;text-decoration:underline;text-underline-offset:5px}
.mainnav .phone{display:flex;align-items:center;gap:8px}
.hero h1{position:absolute;left:80px;top:224px;width:560px;font-size:38px;line-height:46px;font-weight:600;color:var(--white)}
.btn{position:absolute;display:flex;align-items:center;justify-content:center;font-size:13px;font-weight:500}
.btn-ghost-light{border:2px solid var(--white);color:var(--white)}
.btn-solid{background:var(--blue);color:var(--white);box-shadow:0 3px 6px rgba(0,0,0,.18)}
.btn-outline{border:1.5px solid var(--blue);color:var(--blue);background:var(--white)}
.round{position:absolute;border-radius:50%;display:flex;align-items:center;justify-content:center}
.dots{position:absolute;left:566px;top:588px;display:flex;gap:8px}
.dots span{width:11px;height:11px;border:1.5px solid var(--white);border-radius:50%}
.dots span.on{background:var(--white)}

/* sections */
.eyebrow{position:absolute;width:1200px;text-align:center;font-size:13px;font-weight:500;color:#555}
.welcome-title{position:absolute;left:0;top:738px;width:1200px;text-align:center;font-size:24px;line-height:29px;font-weight:500}
.welcome-title span{color:var(--blue)}
.welcome-copy{position:absolute;left:200px;top:851px;width:800px;text-align:center;font-size:14px;line-height:19px;color:var(--muted)}

.products{position:absolute;left:0;top:1026px;width:1200px;height:480px;background:var(--soft)}
.products h2{position:absolute;top:90px;width:1200px;text-align:center;font-size:24px;font-weight:500}
.card{position:absolute;top:146px;width:280px;height:200px;display:flex;align-items:flex-end;justify-content:center;padding-bottom:18px;color:var(--white);font-size:18px;font-weight:600}
.card.gel{left:156px;background:linear-gradient(160deg,#d9cbb4,#9c8a6e)}
.card.petal{left:459px;background:linear-gradient(160deg,#8a6a55,#4f3a2c);align-items:center;flex-direction:column;padding:0;justify-content:center;gap:10px}
.card.foam{left:763px;background:linear-gradient(160deg,#9a8fd6,#e6e3ef)}

.services-label{position:absolute;left:80px;top:1570px;font-size:13px;font-weight:500;color:#555}
.services h2{position:absolute;left:80px;top:1605px;width:470px;font-size:24px;line-height:29px;font-weight:500}
.ticks{position:absolute;left:80px;top:1720px;width:490px;list-style:none;font-size:12px;line-height:15px;color:#555}
.ticks li{display:flex;gap:8px;margin-bottom:9px}
.ticks svg{flex:none;margin-top:2px}
.services-photo{position:absolute;left:612px;top:1570px;width:508px;height:423px;background:linear-gradient(135deg,#e9eef3 0%,#f4f2ef 40%,#7cc9e6 100%)}

.clients{position:absolute;top:2101px;left:156px;display:flex;gap:18px}
.client{width:163px;height:80px;background:#f2f4f6;display:flex;align-items:center;justify-content:center;gap:8px;font-size:20px;font-weight:600;color:#3a3f44}
.client i{width:16px;height:16px;border-radius:50%;background:var(--blue);display:block}

/* footer */
.footer{position:absolute;left:0;top:2247px;width:1200px;height:362px;background:var(--footer);color:var(--footer-text)}
.footer .brand{left:80px;top:66px;color:var(--blue)}
.footer .brand-dot{width:44px;height:44px;background:var(--blue)}
.footer .brand-name{font-size:26px}
.f-contact{position:absolute;left:80px;top:148px;font-size:13px;line-height:20px}
.f-contact .tel{color:var(--blue);font-size:16px;font-weight:600;margin-bottom:4px}
.f-contact .mail{text-decoration:underline}
.f-contact .addr{margin-top:14px;line-height:20px}
.fcol{position:absolute;top:64px}
.fcol h3{font-size:14px;font-weight:600;color:var(--blue);margin-bottom:12px}
.fcol a{display:block;font-size:12px;line-height:29px}
.fcol a.active{color:var(--blue)}
.subscribe{position:absolute;left:861px;top:92px;width:259px;height:36px;border:1px solid #777;display:flex;align-items:center;justify-content:space-between;padding:0 12px;font-size:11px;color:#9a9a9a}
.socials{position:absolute;left:861px;top:152px;display:flex;gap:10px}
.socials span{width:32px;height:32px;border-radius:50%;background:#e6e6e6;display:block}
.socials span.on{background:var(--blue)}
.footer .btn-outline{background:transparent}
.f-rule{position:absolute;left:80px;top:302px;width:1040px;height:1px;background:#5c5c5c}
.copy{position:absolute;left:80px;top:324px;font-size:12px}
.copy span{color:var(--blue)}
</style>
</head>
<body>

<header class="hero" role="img" aria-label="Lush green flowering shrub in soft natural light">
  <div class="brand">
    <div class="brand-dot"></div>
    <div><div class="brand-name">Aroma Nest</div><div class="brand-sub">Master Perfumers</div></div>
  </div>
  <nav class="topnav"><a>Blog</a><a>Online Training</a><a>Careers</a></nav>
  <svg class="search" width="12" height="12" viewBox="0 0 12 12" fill="none" stroke="#fff" stroke-width="1.5"><circle cx="5" cy="5" r="3.8"/><path d="M8 8l3 3"/></svg>
  <nav class="mainnav">
    <a>Home</a><a>About Us</a><a>Products</a><a>Services</a><a>Contact Us</a>
    <a class="phone"><svg width="13" height="13" viewBox="0 0 24 24" fill="none" stroke="#fff" stroke-width="2"><path d="M22 17v3a2 2 0 0 1-2 2A19 19 0 0 1 2 4a2 2 0 0 1 2-2h3l2 5-2.5 1.5a11 11 0 0 0 6 6L14 12l5 2z"/></svg>(+27)010 555 0148</a>
  </nav>
  <h1>Contrary to popular lorem ipsum is not simply random text!</h1>
  <a class="btn btn-ghost-light" style="left:80px;top:397px;width:143px;height:36px">Explore More</a>
  <span class="round" style="left:1088px;top:309px;width:31px;height:31px;border:1.5px solid #fff">
    <svg width="12" height="10" viewBox="0 0 12 10" fill="none" stroke="#fff" stroke-width="1.5"><path d="M11 5H1M5 1L1 5l4 4"/></svg></span>
  <span class="round" style="left:1088px;top:348px;width:31px;height:31px;background:var(--blue)">
    <svg width="12" height="10" viewBox="0 0 12 10" fill="none" stroke="#fff" stroke-width="1.5"><path d="M1 5h10M7 1l4 4-4 4"/></svg></span>
  <div class="dots"><span></span><span class="on"></span><span></span><span></span></div>
</header>

<section class="welcome">
  <p class="eyebrow" style="top:702px">Welcome to</p>
  <h2 class="welcome-title"><span>Aroma Nest</span> supplies Fine Fragrance aroma<br>compounds as pure “A” Grade perfume oil to manufacturers<br>of perfumes in Southern, Eastern and Central Africa.</h2>
  <p class="welcome-copy">Not only does Aroma Nest supply the perfume oil but we also offer expert advice on mixing, formulating and packaging for perfume products ...</p>
  <a class="btn btn-solid" style="left:527px;top:923px;width:144px;height:37px">Discover About</a>
</section>

<section class="products">
  <p class="eyebrow" style="top:61px">Our Products</p>
  <h2>Browse our oils for perfume below</h2>
  <span class="round" style="left:99px;top:229px;width:32px;height:32px;border:1.5px solid var(--blue);background:#fff">
    <svg width="12" height="10" viewBox="0 0 12 10" fill="none" stroke="#2f9fd9" stroke-width="1.5"><path d="M11 5H1M5 1L1 5l4 4"/></svg></span>
  <div class="card gel" role="img" aria-label="Shower gel bottles in a woven basket">Shower Gel</div>
  <div class="card petal" role="img" aria-label="Perfume oil vials with white blossoms"><span>Petalune</span></div>
  <div class="card foam" role="img" aria-label="Lavender foam bath bottle on soft towels">Foam Bath</div>
  <span class="round" style="left:1066px;top:229px;width:32px;height:32px;background:var(--blue)">
    <svg width="12" height="10" viewBox="0 0 12 10" fill="none" stroke="#fff" stroke-width="1.5"><path d="M1 5h10M7 1l4 4-4 4"/></svg></span>
  <a class="btn btn-outline" style="left:529px;top:379px;width:142px;height:37px">All Products</a>
</section>

<section class="services">
  <p class="services-label">Our Services</p>
  <h2>We have expertise to manufacture fragrance oils from a concept to a reality.</h2>
  <ul class="ticks">
    <li><svg width="11" height="11" viewBox="0 0 12 12" fill="none" stroke="#2f9fd9"><circle cx="6" cy="6" r="5.3"/><path d="M3.5 6l1.8 1.8L8.5 4.5"/></svg>Fragrance Matching Services (GCMS)</li>
    <li><svg width="11" height="11" viewBox="0 0 12 12" fill="none" stroke="#2f9fd9"><circle cx="6" cy="6" r="5.3"/><path d="M3.5 6l1.8 1.8L8.5 4.5"/></svg>Locally manufactured FMCG fragrances</li>
    <li><svg width="11" height="11" viewBox="0 0 12 12" fill="none" stroke="#2f9fd9"><circle cx="6" cy="6" r="5.3"/><path d="M3.5 6l1.8 1.8L8.5 4.5"/></svg>Small Minimum Order Quantity (10KG)</li>
    <li><svg width="11" height="11" viewBox="0 0 12 12" fill="none" stroke="#2f9fd9"><circle cx="6" cy="6" r="5.3"/><path d="M3.5 6l1.8 1.8L8.5 4.5"/></svg>Global sourcing of Fine and FMCG fragrances from some of the worlds biggest manufacturers</li>
    <li><svg width="11" height="11" viewBox="0 0 12 12" fill="none" stroke="#2f9fd9"><circle cx="6" cy="6" r="5.3"/><path d="M3.5 6l1.8 1.8L8.5 4.5"/></svg>Product Formulation Advice</li>
    <li><svg width="11" height="11" viewBox="0 0 12 12" fill="none" stroke="#2f9fd9"><circle cx="6" cy="6" r="5.3"/><path d="M3.5 6l1.8 1.8L8.5 4.5"/></svg>Partnership with a leading packaging supplier to suit your product packaging needs</li>
    <li><svg width="11" height="11" viewBox="0 0 12 12" fill="none" stroke="#2f9fd9"><circle cx="6" cy="6" r="5.3"/><path d="M3.5 6l1.8 1.8L8.5 4.5"/></svg>Partnership with a leading Ethanol supplier for fine fragrance product application</li>
  </ul>
  <a class="btn btn-outline" style="left:80px;top:1955px;width:143px;height:37px">Contact Us</a>
  <div class="services-photo" role="img" aria-label="Rolled white towel, cherry blossom sprig and blue bath salts"></div>
</section>

<section class="clients-section">
  <p class="eyebrow" style="top:2056px">Our Clients</p>
  <svg class="abs" style="left:122px;top:2135px" width="8" height="12" viewBox="0 0 8 12" fill="#888"><path d="M7 0v12L0 6z"/></svg>
  <div class="clients">
    <div class="client"><i></i>Valdoret</div>
    <div class="client">Lunare</div>
    <div class="client">Castello</div>
    <div class="client">Orivance</div>
    <div class="client">Morvaleth</div>
  </div>
  <svg class="abs" style="left:1066px;top:2135px" width="8" height="12" viewBox="0 0 8 12" fill="#2f9fd9"><path d="M1 0v12l7-6z"/></svg>
</section>

<footer class="footer">
  <div class="brand">
    <div class="brand-dot"></div>
    <div><div class="brand-name">Aroma Nest</div><div class="brand-sub" style="color:#c9c9c9">Master Perfumers</div></div>
  </div>
  <div class="f-contact">
    <p class="tel">P: +27(0) 10 555 0148</p>
    <p class="mail">info@aromanest.example</p>
    <p class="addr">Unit 4, 12 Fernhill Road, Lakeside View,<br>Greenvale 1650</p>
  </div>
  <div class="fcol" style="left:424px"><h3>Aroma Nest</h3><a>Home</a><a class="active">About Us</a><a>Products</a><a>Services</a><a>Contact Us</a></div>
  <div class="fcol" style="left:626px"><h3>Quick Links</h3><a>Blog</a><a>Online Training</a><a>Careers</a><a>Terms of Use</a><a>Privacy Policy</a></div>
  <div class="fcol" style="left:861px"><h3>Subscribe Us</h3></div>
  <div class="subscribe"><span>Your Email ...</span>
    <svg width="12" height="10" viewBox="0 0 12 10" fill="none" stroke="#ddd" stroke-width="1.5"><path d="M1 5h10M7 1l4 4-4 4"/></svg></div>
  <div class="socials" aria-label="Social links"><span></span><span class="on"></span><span></span><span></span></div>
  <a class="btn btn-outline" style="left:861px;top:216px;width:144px;height:37px">Call Me Back</a>
  <span class="round" style="left:1066px;top:276px;width:52px;height:52px;background:var(--blue)">
    <svg width="26" height="22" viewBox="0 0 26 22" fill="none" stroke="#fff" stroke-width="1.8"><path d="M3 3h14v9H9l-4 3v-3H3z"/><path d="M19 7h4v9h-2v3l-4-3h-6v-2"/></svg></span>
  <div class="f-rule"></div>
  <p class="copy">© 2018 <span>Aroma Nest</span>. All Rights Reserved.</p>
</footer>

</body>
</html>
```